Coastal Heritage Dairywrights' Guild needs new business cards

We need new business cards designed and produced. We are likely to need other design work done for ads, flyers etc in future.

We would like to start with an initial business card.

The Coastal Heritage Dairywrights' Guild (CHDG) is a membership-based not-for-profit organisation that looks after the interests of Australia's small to medium artisan cheesemakers, many of whom are also small-scale farmers. The design should be simple, using our logo, but also communicate our artisan cheese and small dairy farm focus.

The first card to be designed and produced is for me, Megan Thorburn. My details are:

Megan Thorburn
Secretary
Coastal Heritage Dairywrights' Guild (CHDG)
http://www.curdandcrockery.org
T +61427583914
E megan.meganthorburn@mailfern.net

I have attached the CHDG logo in jpg form. I have a higher resolution version available if needed.

Thank you!

Megan

Business

Megan Thorburn
Coastal Heritage Dairywrights' Guild
megan.meganthorburn@mailfern.net
+61427583914

Sans Serif

• Logo (see attached file)

```html
<!DOCTYPE html>
<html lang="en">
<head>
<meta charset="utf-8">
<title>Megan Thorburn – Business Card</title>
<link rel="stylesheet" href="https://fonts.googleapis.com/css2?family=Marcellus&family=Open+Sans:wght@400&display=swap">
<style>
  :root {
    --backdrop: #e8e3dd;
    --card-orange: #e57636;
    --card-orange-light: #ea8a52;
    --ink-white: #ffffff;
    --cheese-yellow: #f6c869;
  }
  * { box-sizing: border-box; margin: 0; padding: 0; }
  html, body {
    width: 1200px; height: 1015px; overflow: hidden;
    background: var(--backdrop);
  }
  .business-card {
    position: absolute; left: 75px; top: 207px;
    width: 1050px; height: 600px;
    border-radius: 40px;
    background: linear-gradient(120deg, var(--card-orange) 0%, var(--card-orange) 45%, var(--card-orange-light) 60%, var(--card-orange) 75%);
    box-shadow: 0 18px 40px rgba(0,0,0,0.25);
    color: var(--ink-white);
  }
  .stitched-frame { position: absolute; inset: 0; }
  .holder-name {
    position: absolute; left: 150px; top: 105px;
    font: 48px "Marcellus", serif;
    letter-spacing: 5px; text-transform: uppercase;
  }
  .holder-org {
    position: absolute; left: 140px; top: 168px;
    font: 23px "Open Sans", sans-serif;
    letter-spacing: 0.3px;
  }
  .contact-list {
    position: absolute; left: 215px; top: 250px;
    list-style: none;
    font: 25px "Open Sans", sans-serif;
    letter-spacing: 0.5px;
  }
  .contact-list li { display: flex; align-items: center; gap: 8px; height: 36px; }
  .contact-icon { width: 30px; height: 30px; flex: none; }
  .guild-mark {
    position: absolute; left: 640px; top: 380px;
    display: flex; align-items: center; gap: 22px;
  }
  .guild-dot {
    width: 110px; height: 110px; border-radius: 50%;
    background: var(--cheese-yellow);
    flex: none;
  }
  .guild-name {
    font: 36px/1.12 "Marcellus", serif;
    letter-spacing: 2px;
  }
</style>
</head>
<body>
  <article class="business-card">
    <svg class="stitched-frame" viewBox="0 0 1050 600" width="1050" height="600" aria-hidden="true">
      <path d="M82,35 H968 A47,47 0 0 0 1015,82 V518 A47,47 0 0 0 968,565 H82 A47,47 0 0 0 35,518 V82 A47,47 0 0 0 82,35 Z"
            fill="none" stroke="#fff" stroke-width="3.5" stroke-dasharray="9 7"/>
    </svg>

    <h1 class="holder-name">Megan Thorburn</h1>
    <p class="holder-org">Coastal Heritage Dairywrights' Guild</p>

    <ul class="contact-list">
      <li>
        <svg class="contact-icon" viewBox="0 0 30 30" aria-hidden="true">
          <circle cx="15" cy="15" r="13" fill="none" stroke="#fff" stroke-width="2"/>
          <path d="M10,8 l3,0 1,4 -2,1.5 q1.5,3 4.5,4.5 l1.5,-2 4,1 0,3 q-1,2 -3,2 q-7,-1 -10,-9 q0,-3 1,-5z" fill="#fff"/>
        </svg>
        <span>megan.meganthorburn@mailfern.net</span>
      </li>
      <li>
        <svg class="contact-icon" viewBox="0 0 30 30" aria-hidden="true">
          <circle cx="15" cy="15" r="13" fill="none" stroke="#fff" stroke-width="2"/>
          <rect x="7.5" y="10" width="15" height="10" fill="none" stroke="#fff" stroke-width="1.6"/>
          <path d="M7.5,10 L15,16 L22.5,10 M7.5,20 L12.5,15 M22.5,20 L17.5,15" fill="none" stroke="#fff" stroke-width="1.4"/>
        </svg>
        <span>+61427583914</span>
      </li>
    </ul>

    <div class="guild-mark">
      <span class="guild-dot"></span>
      <p class="guild-name">Coastal<br>Heritage<br>Dairywrights'<br>Guild</p>
    </div>
  </article>
</body>
</html>
```